Virtual Assistant/Online Marketing Business Card/Stationary

I need a professional but modern business card/stationary for my company in Dallas called Brivolo. Brivolo is a virtual assistant specializing in online marketing. I would like a unique design that stands out and makes my brand clear. Incorporating the logo is a must and have attached it to this brief.

Target Market(s)

small business owners & entrepreneurs, 35-65

Industry/Entity Type

Business

Contact Information for Business Card

Maren Tolk
marentolk@brivolo.biz
(555) 271-9064
brivolo.biz

Font styles to use
Sans Serif

Colors
f04a50
3176b5
9bcb3c

Requirements
Must have
• Colors that match the logo colors. Logo integration

```html
<!DOCTYPE html>
<html lang="en">
<head>
<meta charset="utf-8">
<title>Brivolo Business Card</title>
<link rel="stylesheet" href="https://fonts.googleapis.com/css2?family=Open+Sans:wght@400;700&family=Roboto:wght@400;700&display=swap">
<style>
  :root {
    --page: #ffffff;
    --stage: #d3d4d6;
    --card-light: #e9eaeb;
    --card-light-tone: #dcdee0;
    --band-dark: #222426;
    --card-dark: #414141;
    --card-dark-tone: #5e5e5e;
    --ink-dark: #231f20;
    --ink-light: #ffffff;
    --ink-soft: #e6e6e6;
    --brand-red: #f04a50;
    --brand-blue: #3176b5;
    --brand-green: #9bcb3c;
    --tint-red: rgba(240, 74, 80, 0.22);
    --tint-blue: rgba(49, 118, 181, 0.18);
    --tint-green: rgba(155, 203, 60, 0.25);
  }
  * { box-sizing: border-box; margin: 0; padding: 0; }
  html, body {
    width: 1200px;
    height: 440px;
    overflow: hidden;
    background: var(--page);
  }
  .canvas {
    position: relative;
    width: 1200px;
    height: 440px;
  }
  .stage {
    position: absolute;
    left: 12px;
    top: 42px;
    width: 1178px;
    height: 356px;
    background: var(--stage);
  }
  .card {
    position: absolute;
    border-radius: 0 34px 0 34px;
    overflow: hidden;
  }

  /* Front face */
  .card-front {
    left: 21px;
    top: 48px;
    width: 561px;
    height: 343px;
    background: linear-gradient(160deg, var(--card-light) 0%, var(--card-light-tone) 100%);
  }
  .front-decoration {
    position: absolute;
    inset: 0 0 58px 0;
    background:
      linear-gradient(163deg,
        transparent 0%,
        transparent 34%,
        var(--tint-green) 44%,
        var(--tint-green) 50%,
        var(--tint-red) 56%,
        var(--tint-red) 70%,
        transparent 76%,
        var(--tint-blue) 84%,
        var(--tint-blue) 92%,
        transparent 100%);
  }
  .front-brand {
    position: absolute;
    left: 0;
    right: 0;
    top: 168px;
    display: flex;
    align-items: center;
    justify-content: center;
    gap: 12px;
  }
  .brand-dot {
    width: 20px;
    height: 20px;
    border-radius: 50%;
    background: var(--brand-red);
  }
  .front-wordmark {
    font-family: "Open Sans", sans-serif;
    font-weight: 700;
    font-size: 66px;
    line-height: 1;
    letter-spacing: -1px;
    color: var(--ink-dark);
  }
  .front-band {
    position: absolute;
    left: 0;
    right: 0;
    bottom: 0;
    height: 58px;
    background: var(--band-dark);
    display: flex;
    align-items: center;
    justify-content: center;
    font-family: "Open Sans", sans-serif;
    font-size: 24px;
    color: var(--ink-light);
  }

  /* Back face */
  .card-back {
    left: 620px;
    top: 48px;
    width: 567px;
    height: 336px;
    background: var(--card-dark);
  }
  .back-decoration {
    position: absolute;
    right: 0;
    bottom: 0;
    width: 440px;
    height: 200px;
    background: linear-gradient(160deg,
      transparent 0%,
      transparent 35%,
      var(--card-dark-tone) 55%,
      var(--card-dark) 68%,
      var(--card-dark-tone) 82%,
      transparent 100%);
    opacity: 0.8;
  }
  .contact {
    position: absolute;
    right: 18px;
    top: 22px;
    text-align: right;
    font-family: "Roboto", sans-serif;
    color: var(--ink-light);
  }
  .contact-name {
    font-size: 31px;
    line-height: 1.1;
    text-transform: uppercase;
    font-weight: 400;
    margin-bottom: 6px;
  }
  .contact-name strong { font-weight: 700; }
  .contact-line {
    font-size: 11.5px;
    line-height: 1.4;
    color: var(--ink-soft);
    padding-right: 8px;
  }
  .back-brand {
    position: absolute;
    left: 44px;
    top: 198px;
    display: flex;
    align-items: center;
    gap: 12px;
  }
  .back-brand .brand-dot { background: var(--brand-green); }
  .back-wordmark {
    font-family: "Open Sans", sans-serif;
    font-weight: 700;
    font-size: 64px;
    line-height: 1;
    letter-spacing: -1px;
    color: var(--ink-light);
  }
</style>
</head>
<body>
  <main class="canvas">
    <div class="stage"></div>

    <section class="card card-front" aria-label="Card front">
      <div class="front-decoration" role="img" aria-label="Soft sweeping bands in brand green, red and blue over a light grey diamond pattern"></div>
      <div class="front-brand">
        <span class="brand-dot"></span>
        <span class="front-wordmark">Brivolo</span>
      </div>
      <div class="front-band">brivolo.biz</div>
    </section>

    <section class="card card-back" aria-label="Card back">
      <div class="back-decoration" role="img" aria-label="Faint grey sweeping bands"></div>
      <div class="contact">
        <h1 class="contact-name"><strong>Maren</strong> Tolk</h1>
        <p class="contact-line">marentolk@brivolo.biz</p>
        <p class="contact-line">(555) 271-9064</p>
      </div>
      <div class="back-brand">
        <span class="brand-dot"></span>
        <span class="back-wordmark">Brivolo</span>
      </div>
    </section>
  </main>
</body>
</html>
```